Brightwater Kinetics (formerly qzt7)

I'm doing a totally different business card now! I recently made some adjustments to my companies moving forward due to outstanding events. Because of this I will be increasing the prize money to the winner and second place.

Here is my new concept.

Brightwater Kinetics
Empowering futures.

My company will be in the following areas:
marketing & innovation, leadership & communication, energy & technology, culture & community, luxury & living.

I do not have a logo - so that is a must! Be creative and you will be rewarded!

I am looking for edgy, big, professional, dynamic!

One idea I had for the logo is a Brightwater symbol (needs to be created) and the shadow of words that describe my business (see above) behind it on one side and then the information on the other.

Go big - go nuts - be creative - YOU ROCK!

Target Market(s)

Multi-billion dollar corporations, world leaders, high end investors, millionaire entrepreneurs

Industry/Entity Type

Leadership

Requirements
Must have
• Name, title, phone, email, website, space for Qr code

Nice to have
• design on front and back. Possible the logo on one side and info on the other.

```html
<!DOCTYPE html>
<html lang="en">
<head>
<meta charset="utf-8">
<title>Brightwater Kinetics – Business Card</title>
<link rel="stylesheet" href="https://fonts.googleapis.com/css2?family=Montserrat:wght@300;400;700&display=swap">
<style>
  :root {
    --sheet: #ffffff;
    --sheet-rule: #8a8a8a;
    --card: #0b0b0c;
    --silver-dark: #9a9a9c;
    --silver-mid: #c9c9cb;
    --silver-light: #f4f4f5;
    --text: #e9e9ea;
    --text-soft: #d2d2d4;
  }
  * { box-sizing: border-box; margin: 0; padding: 0; }
  html, body { width: 1200px; height: 833px; overflow: hidden; background: var(--sheet); }
  body { position: relative; font-family: "Montserrat", sans-serif; }

  .sheet-frame {
    position: absolute; left: 1px; top: 1px; width: 1198px; height: 831px;
    border: 1px solid var(--sheet-rule);
  }

  .card {
    position: absolute; width: 564px; height: 323px;
    background: var(--card); border-radius: 10px; overflow: hidden;
  }
  .card--front { left: 203px; top: 69px; }
  .card--back  { left: 439px; top: 432px; }

  .card__band {
    position: absolute; left: 0; width: 100%; height: 11px;
    background: linear-gradient(90deg, var(--silver-dark) 0%, var(--silver-mid) 18%, var(--silver-light) 50%, var(--silver-mid) 82%, var(--silver-dark) 100%);
  }
  .card__band--top { top: 0; }
  .card__band--bottom { bottom: 0; }

  .brand__mark {
    position: absolute; border: 2px solid var(--text-soft); border-radius: 50%;
  }
  .brand__name {
    position: absolute; font-weight: 700; color: var(--text); white-space: nowrap; line-height: 1.25;
  }

  /* front */
  .card--front .brand__mark { left: 90px; top: 138px; width: 72px; height: 72px; }
  .card--front .brand__name { left: 180px; top: 140px; font-size: 28px; letter-spacing: 1.5px; }

  /* back */
  .card--back .brand__mark { left: 30px; top: 40px; width: 44px; height: 44px; }
  .card--back .brand__name { left: 86px; top: 38px; font-size: 17px; letter-spacing: 1px; }

  .holder-name {
    position: absolute; left: 380px; top: 40px; font-size: 13px; font-weight: 400;
    letter-spacing: 1px; color: var(--text);
  }

  .services { position: absolute; left: 32px; top: 108px; list-style: none; }
  .services li { font-size: 11.5px; font-weight: 300; line-height: 16px; color: var(--text-soft); }

  .contact {
    position: absolute; left: 330px; top: 221px; border-collapse: collapse;
    font-size: 12px; font-weight: 300; color: var(--text-soft);
  }
  .contact th { text-align: left; font-weight: 300; width: 81px; height: 20px; padding: 0; }
  .contact td { font-size: 11px; padding: 0; white-space: nowrap; }
</style>
</head>
<body>
  <div class="sheet-frame"></div>

  <section class="card card--front" aria-label="Card front">
    <div class="card__band card__band--top"></div>
    <div class="brand__mark"></div>
    <div class="brand__name">BRIGHTWATER<br>KINETICS</div>
    <div class="card__band card__band--bottom"></div>
  </section>

  <section class="card card--back" aria-label="Card back">
    <div class="card__band card__band--top"></div>
    <div class="brand__mark"></div>
    <div class="brand__name">BRIGHTWATER<br>KINETICS</div>

    <div class="holder-name">XXXXXXXXXXXXXXX</div>

    <ul class="services">
      <li>Marketing &amp; Innovation</li>
      <li>Leadership &amp; Communication</li>
      <li>Energy &amp; Technology</li>
      <li>Culture &amp; Community</li>
      <li>Luxury &amp; Living</li>
    </ul>

    <table class="contact">
      <tr><th>Toll free</th><td>: xxxxxxxxxxxx</td></tr>
      <tr><th>Fax</th><td>: xxxxxxxxxxxxxx</td></tr>
      <tr><th>Email</th><td>: xxxxxxxxxxxx.com</td></tr>
      <tr><th>Web</th><td>: www.xxxxxxxxxx.com</td></tr>
    </table>
    <div class="card__band card__band--bottom"></div>
  </section>
</body>
</html>
```